Print & Packaging Design for Snacks and logo for Brotés Snacks

Print & Packaging Design for Snacks

The product is for a spanish speaking country.

Design guidelines:

The purpose of this brief is creation of the artwork design for packaging of:
a) Rodajas de Papa Frita (Potato chips)
b) Palitos de Queso (Corn flips, puffed corn snack)
c) Tortillas (Tortillas Chips)
d) Rodajas de Platano Frito (Plantain Chips)

The Brand name will be "Brotés" we have no logo, so you will need to combine the logo with the packaging Ideas you will be developing. you will be free to combine any color and texture you like. We are looking for a modern and healthy look. Dont be so heaving user of red, yellow, etc. Use more whilte and combine it with the colors you like.

All four have common theme which is: "Siempre Frescos!" (Always fresh, in local language). Fresh refers to the freshness of the product that originates from local production and quick distribution after the production.

I will let you use your imagination, to combine colors, textures and images.

Space for communication of variant should be made in the bottom right corner.

The back side of all three products must be reserved for:
a) Explanation on what fresh and home-made mean (a short story in not more than 40 words; as explained in the beginning; exact wording will be added later)
b) Nutritional information table (will be added later)
c) Contents and producer/importer data in multiple languages will be added later)

Dimension of packages: Small 16X22cm and Large 16X33
Finished work should be delivered in vector, layered format for further editing with respect to possibility of inserting/modifying information on product content, calorie values, importer/distributor data, packaging size, expiration date etc and a 3d rendering of how might the product look.

```html
<!DOCTYPE html>
<html lang="es">
<head>
<meta charset="UTF-8">
<title>Brotés — Rodajas de Papa Frita</title>
<link rel="stylesheet" href="https://fonts.googleapis.com/css2?family=Roboto+Slab:wght@300;400;700;800&display=swap">
<style>
  :root {
    --stage: #ecebf1;
    --pack-white: #f7f7f7;
    --pack-shade: #e6e6e6;
    --brand-red: #c8102e;
    --band-red: #d9252b;
    --band-yellow: #f2c21b;
    --band-green: #4a9a2c;
    --band-lime: #9ccc3a;
    --fresh-green: #2f7d2a;
    --ink-grey: #555555;
    --chip-light: #f4d67a;
    --chip-deep: #dd9a3a;
    --leaf-light: #6bb64a;
    --leaf-deep: #2e7a27;
  }
  * { margin: 0; padding: 0; box-sizing: border-box; }
  html, body { width: 1200px; height: 900px; overflow: hidden; }
  body {
    background: var(--stage);
    font-family: "Roboto Slab", Georgia, serif;
    position: relative;
  }
  .pack-front {
    position: absolute;
    left: 340px; top: 92px;
    width: 520px; height: 715px;
    background: linear-gradient(180deg, var(--pack-white) 0%, #ffffff 45%, var(--pack-shade) 100%);
    overflow: hidden;
    box-shadow: 0 10px 30px rgba(0,0,0,0.12);
  }
  .band { position: absolute; left: 0; width: 100%; }
  .band-top { top: 0; height: 90px; }
  .band-bottom { bottom: 0; height: 110px; }

  .flavour-corner {
    position: absolute; right: -70px; top: -70px;
    width: 160px; height: 160px; border-radius: 50%;
    background: var(--brand-red);
  }
  .flavour-corner-text {
    position: absolute; right: 2px; top: 22px;
    transform: rotate(45deg);
    color: #fff; font-size: 12px; font-weight: 700; line-height: 1.15;
    text-align: center; letter-spacing: 1px;
  }

  .brand-name {
    position: absolute; left: 0; top: 160px; width: 100%;
    text-align: center;
    font-size: 124px; font-weight: 800; line-height: 1;
    color: var(--brand-red);
    letter-spacing: -2px;
  }

  .product-name {
    position: absolute; left: 34px; top: 302px;
    color: var(--ink-grey); font-weight: 300; line-height: 1.05;
  }
  .product-name .line-small { display: block; font-size: 28px; padding-left: 12px; }
  .product-name .line-large { display: block; font-size: 36px; }

  .fresh-seal {
    position: absolute; left: 304px; top: 262px;
    width: 184px; height: 184px; border-radius: 50%;
    background: #ffffff;
    border: 2px dashed #dcdcdc;
    text-align: center; color: var(--fresh-green);
  }
  .fresh-seal .seal-small { display: block; margin-top: 44px; font-size: 15px; letter-spacing: 6px; font-weight: 400; }
  .fresh-seal .seal-large { display: block; font-size: 30px; font-weight: 800; line-height: 1.1; }
  .fresh-seal .seal-ribbon {
    display: inline-block; margin-top: 8px;
    background: var(--fresh-green); color: #fff;
    font-size: 10px; font-weight: 700; letter-spacing: 1px;
    padding: 3px 14px;
    clip-path: polygon(0 0, 100% 0, 92% 50%, 100% 100%, 0 100%, 8% 50%);
  }

  .leaf-art {
    position: absolute;
    background: linear-gradient(135deg, var(--leaf-light), var(--leaf-deep));
    border-radius: 0 70% 0 70%;
  }
  .leaf-art.left { left: 240px; top: 332px; width: 62px; height: 52px; }
  .leaf-art.right { left: 432px; top: 420px; width: 64px; height: 56px; transform: rotate(80deg); }

  .chips-photo {
    position: absolute; left: 0; top: 395px;
    width: 100%; height: 260px;
    background: radial-gradient(ellipse at 50% 40%, var(--chip-light) 0%, #eebf5c 55%, var(--chip-deep) 100%);
  }
</style>
</head>
<body>
  <main class="pack-front">
    <svg class="band band-top" viewBox="0 0 520 90" preserveAspectRatio="none" aria-hidden="true">
      <path d="M0 0 H520 V20 C400 30 250 10 0 70 Z" fill="var(--band-red)"/>
      <path d="M0 70 C200 20 380 28 520 20 V34 C380 40 210 40 0 82 Z" fill="var(--band-yellow)"/>
      <path d="M0 82 C200 44 380 44 520 34 V48 C380 56 220 58 0 90 Z" fill="var(--band-green)"/>
    </svg>

    <div class="flavour-corner"></div>
    <div class="flavour-corner-text">SABOR<br>ORIGINAL</div>

    <h1 class="brand-name">Brotés</h1>

    <p class="product-name">
      <span class="line-small">Rodajas de</span>
      <span class="line-large">Papa Frita</span>
    </p>

    <div class="leaf-art left" role="img" aria-label="Hojas verdes decorativas"></div>

    <div class="fresh-seal">
      <span class="seal-small">SIEMPRE</span>
      <span class="seal-large">FRESCOS</span>
      <span class="seal-ribbon">100% NATURAL</span>
    </div>

    <div class="leaf-art right" role="img" aria-label="Hojas verdes decorativas"></div>

    <div class="chips-photo" role="img" aria-label="Fotografía de rodajas de papa frita doradas"></div>

    <svg class="band band-bottom" viewBox="0 0 520 110" preserveAspectRatio="none" aria-hidden="true">
      <path d="M0 40 C150 10 330 50 520 0 V30 C330 70 160 40 0 60 Z" fill="var(--band-lime)"/>
      <path d="M0 60 C160 40 330 70 520 30 V60 C330 95 160 70 0 86 Z" fill="var(--band-green)"/>
      <path d="M0 86 C160 70 330 95 520 60 V110 H0 Z" fill="var(--band-red)"/>
    </svg>
  </main>
</body>
</html>
```